Internationally renowned speaker/campaigner needs a book cover

I need a preliminary cover design for my new book "HALF-LIGHT".

I'm a medical doctor and an internationally renowned speaker and campaigner for human-centered and compassionate healthcare, co-founder of an international social movement KINDLING in CLINICS (http://kindlinginclinics.example), and successful author of the book 'PAUSE AND LISTEN - Ways to cherish your practice and your people' (http://www.bookvaultstore.example/PAUSE-LISTEN-cherish-your-practice/dp/9082614530)

The subtitle of HALF-LIGHT is: "How our one-eyed materialistic science leads to inequality, greed, poverty, violence, ill-health and environmental destruction (and what we can do about it)"

Author: Dr GARETH PELLIMORE

Preliminary book blurb:
"As social activists and environmental campaigners we are continuously sabotaging our cause because our strategies are unconsciously supporting the materialistic foundations of our broken world.

Our materialistic science sees the natural world and even people as innate objects, without consciousness or connection. Modern medicine treats patients as broken machines to be fixed, not as conscious, subjective beings. And economic theory says every person is an independent agent, striving to maximize advantage. We turn every human and natural gift into a commodity to be owned, controlled, bought and sold.

Our social policies, education system, justice system and even our democracy assume that incentives, rewards and punishments are the ‘real’ motives for human behavior. Our purpose in life is to ‘get ahead’ and accumulate material goods. Therein lies competition, insecurity, greed, violence, ill-health and the destruction of the natural environment.

Materialistic science is simply blind to the life-world of consciousness, intelligence, purpose and deep interdependence in all natural and human systems. We all know that compassion, kindness, love, and human creativity are the real foundation of our communities, not mindless competition.

But so immersed are we in materialistic assumptions, that in our campaigns we mistakenly adopt tools and strategies from the existing system in our struggle for a better world. But the moment we fight against anything, or demonize our opposition, or sell our ideas for money, or charitably impose our solutions, we only strengthen the material world.

Instead, we have to be the change we want to see: grow an economy of generosity and gifting, freely share ideas, focus on solutions not problems, and deeply believe in the capacity for creativity and healing in every person and every community. You can download this book for free at halflightbook.org."

Design brief
I need a compelling front page image and title design that conveys the idea that our science is one-eyed or half-blind, hence the title name 'half-light', which means half-science.

Our predominant science only sees the material world, not the conscious world. We need both.

I'm also preparing a IDEAx talk on the subject and want the compelling image and title to use for this purpose also.

The genre of books is in the class of leadership, entrepreneurs, positive psychology, community development - and I have uploaded some cover images of books in this class. The cover of my current book, PAUSE AND LISTEN, has elements of the style I'm looking for: bold, bright, simple, metaphorical, a surprising juxtaposition of technical and human.

The way I develop and market the book will be congruent with the ideas expressed. I will give the e-book away for free and invite people to make a donation if they like it (gift economy). The book will be published on the website unfinished, inviting comments, suggestions, stories and ideas to be included in the finished book. So to a degree, the content of the book will be fully developed by crowdsourcing living examples of the core ideas and creating a community of conversation (including a Chatterly page). I'll later be looking for a simple WordPress website design based on the book cover graphic, fonts and colours.

So this first design brief and contract is for an e-book cover and later the book will be self-published as a paperback using PressNest.

Target Market(s)

The target audience is readers who are community leaders and social activists - all those utterly passionate about creating a better world, whether it's in the environment, education, healthcare, violence prevention, justice, health communities, etc.

Font styles to use
Sans Serif

Requirements
Must have
• A compelling image that symbolises the key idea - eyecatching
Should not have
• Must not express 'corporate' concepts, power or hierarchy

```html
<!DOCTYPE html>
<html lang="en">
<head>
<meta charset="utf-8">
<title>HALF-LIGHT — Book Cover</title>
<link rel="stylesheet" href="https://fonts.googleapis.com/css2?family=Oswald:wght@400;700&display=swap">
<style>
  :root {
    --page-bg: #ffffff;
    --cover-top: #ffffff;
    --cover-bottom: #d9d9d9;
    --title-blue: #3d86cc;
    --title-fill-light: #f4f6f8;
    --title-fill-mid: #c9ced4;
    --subtitle-grey: #3a3a3a;
    --author-black: #111111;
    --rope-light: #c9a06a;
    --rope-mid: #9c7440;
    --rope-dark: #6e4e28;
  }
  html, body {
    margin: 0;
    padding: 0;
    width: 1200px;
    height: 1200px;
    overflow: hidden;
    background: var(--page-bg);
  }
  .book-cover {
    position: absolute;
    left: 220px;
    top: 40px;
    width: 760px;
    height: 1120px;
    background: linear-gradient(180deg, var(--cover-top) 0%, var(--cover-top) 45%, var(--cover-bottom) 100%);
    box-shadow: 0 6px 24px rgba(0,0,0,0.18);
    overflow: hidden;
    font-family: "Oswald", "Arial Narrow", sans-serif;
  }
  .cover-title {
    position: absolute;
    top: 70px;
    left: 0;
    width: 100%;
    margin: 0;
    text-align: center;
    font-weight: 700;
    line-height: 0.98;
    letter-spacing: 4px;
  }
  .cover-title .title-line-one {
    display: block;
    font-size: 200px;
    color: var(--title-blue);
  }
  .cover-title .title-line-two {
    display: block;
  }
  .cover-title svg {
    display: block;
    margin: -10px auto 0;
  }
  .cover-subtitle {
    position: absolute;
    top: 500px;
    left: 60px;
    width: 640px;
    margin: 0;
    text-align: center;
    font-weight: 400;
    font-size: 22px;
    line-height: 1.25;
    letter-spacing: 1.2px;
    text-transform: uppercase;
    color: var(--subtitle-grey);
  }
  .cover-illustration {
    position: absolute;
    left: 150px;
    top: 640px;
    width: 460px;
    height: 330px;
    border-radius: 6px;
    background: linear-gradient(160deg, var(--rope-light) 0%, var(--rope-mid) 55%, var(--rope-dark) 100%);
  }
  .author-band {
    position: absolute;
    left: 0;
    top: 992px;
    width: 100%;
    height: 76px;
    background: linear-gradient(90deg, rgba(255,255,255,0) 0%, rgba(255,255,255,0.92) 25%, rgba(255,255,255,0.92) 75%, rgba(255,255,255,0) 100%);
  }
  .author-name {
    position: absolute;
    left: 0;
    top: 1000px;
    width: 100%;
    margin: 0;
    text-align: center;
    font-weight: 700;
    font-size: 38px;
    line-height: 60px;
    letter-spacing: 12px;
    text-transform: uppercase;
    color: var(--author-black);
  }
</style>
</head>
<body>
  <main class="book-cover">
    <h1 class="cover-title">
      <span class="title-line-one">HALF-</span>
      <span class="title-line-two">
        <svg width="640" height="210" viewBox="0 0 640 210" aria-label="LIGHT">
          <defs>
            <linearGradient id="titleFill" x1="0" y1="0" x2="1" y2="1">
              <stop offset="0" stop-color="#f4f6f8"/>
              <stop offset="0.5" stop-color="#c9ced4"/>
              <stop offset="1" stop-color="#f4f6f8"/>
            </linearGradient>
          </defs>
          <text x="320" y="190" text-anchor="middle"
                font-family="Oswald, 'Arial Narrow', sans-serif" font-weight="700"
                font-size="200" letter-spacing="4"
                fill="url(#titleFill)" stroke="#3d86cc" stroke-width="5">LIGHT</text>
        </svg>
      </span>
    </h1>

    <p class="cover-subtitle">
      How our one-eyed materialistic<br>
      science leads to inequality, greed, poverty,<br>
      violence, ill-health and environmental destruction<br>
      (and what we can do about it)
    </p>

    <div class="cover-illustration" role="img" aria-label="Illustration area: a human brain formed from knotted brown rope, with the rope end hanging down"></div>

    <div class="author-band"></div>
    <p class="author-name">Dr GARETH PELLIMORE</p>
  </main>
</body>
</html>
```